■デザインへの要望
1)フライヤーのイメージとしては明るく女性的なイメージを希望します。
2)人物写真は使わないでください。
3)コーポレートロゴを右上に配置してください。
ロゴの改変(色の変更や比率の変更)はご遠慮ください。
4)会のロゴを配置してください。
位置はお任せしますが、サイズの変更はご遠慮ください。
※前回のフライヤーを素材と一緒にお付けしますのでご参考になさってください。

■素材
1)フライヤーを作成する際に必要なロゴ等の画像等は

```html
<!DOCTYPE html>
<html lang="ja">
<head>
<meta charset="utf-8">
<title>ランチョンセミナー15 これからの摂食嚥下障害看護に何が求められているか</title>
<link rel="stylesheet" href="https://fonts.googleapis.com/css2?family=Noto+Sans+JP:wght@400;500;700;900&family=Noto+Serif+JP:wght@500;700;900&display=swap">
<style>
:root{
  --ink:#1f1a1c;
  --pink:#e5609b;
  --pink-soft:#f7c9dc;
  --lavender:#c9b4de;
  --brand-green:#6aa33a;
  --rule:#9a9096;
  --paper:#ffffff;
}
*{margin:0;padding:0;box-sizing:border-box}
html,body{width:846px;height:1200px;overflow:hidden;background:var(--paper)}
.flyer{position:relative;width:846px;height:1200px;overflow:hidden;background:var(--paper);color:var(--ink);font-family:"Noto Sans JP",sans-serif}
.wash{position:absolute;left:0;top:0;width:846px;height:1200px}
.brand{position:absolute;right:26px;top:26px;display:flex;align-items:center;gap:8px;color:var(--brand-green);font-weight:700;font-size:30px;letter-spacing:2px}
.brand-dot{width:16px;height:16px;border-radius:50%;background:var(--brand-green)}
.society{position:absolute;left:96px;top:196px;display:flex;align-items:center;gap:10px;font-size:19px;font-weight:500}
.society-mark{width:30px;height:30px;border-radius:50%;background:var(--pink-soft)}
.seminar-band{position:absolute;left:113px;top:232px;width:627px;height:30px;background:var(--pink);color:#fff;text-align:center;font-size:21px;font-weight:700;line-height:30px;letter-spacing:3px}
.title{position:absolute;left:0;width:846px;top:278px;text-align:center;font-family:"Noto Serif JP",serif;font-weight:900;font-size:60px;line-height:82px;letter-spacing:1px}
.subtitle{position:absolute;left:0;width:846px;top:536px;text-align:center;font-family:"Noto Serif JP",serif;font-weight:700;font-size:28px;line-height:40px}
.subtitle-en{position:absolute;left:0;width:846px;top:582px;text-align:center;font-family:"Noto Serif JP",serif;font-size:17px;font-weight:500;line-height:26px}
.speaker{position:absolute;top:634px;width:280px;height:110px}
.speaker-role{position:absolute;left:0;top:4px;width:26px;height:60px;background:var(--pink);color:#fff;font-size:15px;font-weight:700;writing-mode:vertical-rl;text-align:center;line-height:26px;letter-spacing:6px;display:flex;align-items:center;justify-content:center}
.speaker-name{position:absolute;left:44px;top:0;white-space:nowrap;font-family:"Noto Serif JP",serif;font-weight:900;font-size:36px;line-height:48px}
.speaker-name small{font-size:20px;font-weight:700}
.speaker-aff{position:absolute;left:44px;top:56px;white-space:nowrap;font-size:17px;line-height:26px;font-weight:500}
.speaker-aff.small{font-size:12px;line-height:18px}
.chair{left:135px}
.lecturer{left:431px}
.divider{position:absolute;left:410px;top:638px;width:1px;height:106px;background:var(--rule)}
.label{position:absolute;left:0;width:846px;text-align:center;font-size:19px;font-weight:500;line-height:26px}
.date{position:absolute;left:0;width:846px;top:808px;text-align:center;font-family:"Noto Serif JP",serif;font-weight:900;font-size:50px;line-height:66px}
.date .unit{font-size:30px}
.date .dow{display:inline-block;width:34px;height:34px;border-radius:50%;background:var(--ink);color:#fff;font-size:22px;line-height:34px;vertical-align:8px;font-family:"Noto Sans JP",sans-serif}
.date .time{font-size:32px}
.room{position:absolute;left:0;width:846px;top:904px;text-align:center;font-size:32px;font-weight:900;line-height:44px}
.venue{position:absolute;left:0;width:846px;top:952px;text-align:center;font-size:21px;font-weight:700;line-height:30px}
.footer-rule{position:absolute;left:40px;width:766px;top:1126px;height:1px;background:var(--rule)}
.footer{position:absolute;left:0;width:846px;top:1136px;text-align:center;font-size:15px;line-height:24px}
</style>
</head>
<body>
<main class="flyer">
  <svg class="wash" viewBox="0 0 846 1200" aria-hidden="true">
    <defs>
      <linearGradient id="band" x1="0" y1="0" x2="0" y2="1">
        <stop offset="0" stop-color="#f4a9c8"/>
        <stop offset="0.55" stop-color="#d9b8e4"/>
        <stop offset="1" stop-color="#ffffff" stop-opacity="0"/>
      </linearGradient>
      <radialGradient id="glow" cx="0" cy="0" r="1">
        <stop offset="0" stop-color="#fbe0ec"/>
        <stop offset="1" stop-color="#ffffff" stop-opacity="0"/>
      </radialGradient>
    </defs>
    <rect x="0" y="0" width="420" height="260" fill="url(#glow)"/>
    <rect x="0" y="0" width="70" height="900" fill="url(#band)"/>
    <rect x="70" y="0" width="14" height="700" fill="url(#band)" opacity="0.5"/>
  </svg>

  <div class="brand"><span class="brand-dot"></span>ミラナ</div>

  <div class="society"><span class="society-mark"></span>第25回 日本嚥下ケア研究学会 学術大会</div>
  <div class="seminar-band">ランチョンセミナー 15</div>

  <h1 class="title">これからの<br>摂食嚥下障害看護に<br>何が求められているか</h1>
  <p class="subtitle">――「機能低下予防」と「終末期 Care」――</p>
  <p class="subtitle-en">What is required in the future for dysphagia nursing.</p>

  <section class="speaker chair">
    <span class="speaker-role">座長</span>
    <p class="speaker-name">森川 佳子<small>先生</small></p>
    <p class="speaker-aff">瀬戸内看護大学<br>名誉教授</p>
  </section>
  <div class="divider"></div>
  <section class="speaker lecturer">
    <span class="speaker-role">演者</span>
    <p class="speaker-name">川村 直美<small>先生</small></p>
    <p class="speaker-aff small">公益社団法人 東海看護協会<br>認定看護師教育課程 摂食・嚥下障害看護<br>主任教員</p>
  </section>

  <p class="label" style="top:782px">日時</p>
  <p class="date">2019<span class="unit">年</span>9<span class="unit">月</span>7<span class="unit">日</span><span class="dow">土</span> <span class="time">12:00～13:00</span></p>

  <p class="label" style="top:878px">会場</p>
  <p class="room">第8会場</p>
  <p class="venue">湊メッセ 北浜コンベンションセンター2F【中会議室201】</p>

  <div class="footer-rule"></div>
  <p class="footer">［共催］第25回 日本嚥下ケア研究学会 学術大会<br>ミラナ株式会社</p>
</main>
</body>
</html>
```